RV park billboard

We need a billboard for cedar bend RV park . I was thinking about having a big orange in the background. We will have free fiber optic internet and each camper will have its own personal hotspot and we want that on the sign... Also the phone number with the area code... But I don't have the exact number yet. Size of sign will be 12 x 40
Updates
Make sure sign has Cedar Bend RV park on it
Target Market(s)
Plant turnaround workers
Look and feel

```html
<!DOCTYPE html>
<html lang="en">
<head>
<meta charset="utf-8">
<title>Cedar Bend RV park billboard</title>
<link rel="stylesheet" href="https://fonts.googleapis.com/css2?family=Montserrat:wght@300;400;700&display=swap">
<style>
  :root {
    --page-bg: #eef1f4;
    --orange-light: #ee922e;
    --orange-deep: #e97029;
    --white: #ffffff;
  }
  * { margin: 0; padding: 0; box-sizing: border-box; }
  html, body {
    width: 1200px;
    height: 815px;
    overflow: hidden;
    background: var(--page-bg);
    font-family: "Montserrat", sans-serif;
    color: var(--white);
  }
  .billboard {
    position: absolute;
    left: 40px;
    top: 257px;
    width: 1120px;
    height: 300px;
    display: flex;
  }
  .brand-panel {
    position: relative;
    width: 459px;
    height: 100%;
    background: var(--orange-light);
  }
  .park-name {
    position: absolute;
    left: 23px;
    top: 32px;
    font-size: 26px;
    font-weight: 300;
    letter-spacing: 1px;
    line-height: 1;
  }
  .phone-band {
    position: absolute;
    left: 0;
    top: 193px;
    width: 402px;
    height: 75px;
    background: var(--orange-deep);
    display: flex;
    align-items: center;
    padding-left: 23px;
  }
  .phone-number {
    font-size: 40px;
    font-weight: 700;
    letter-spacing: 0.5px;
    line-height: 1;
  }
  .features-panel {
    position: relative;
    flex: 1;
    height: 100%;
    background: var(--orange-deep);
  }
  .feature-icon {
    position: absolute;
    left: 62px;
    width: 90px;
  }
  .feature-icon--fiber { top: 29px; height: 88px; }
  .feature-icon--wifi { top: 192px; height: 70px; }
  .feature-text {
    position: absolute;
    left: 203px;
    line-height: 1;
  }
  .feature-text--fiber { top: 33px; }
  .feature-text--wifi { top: 188px; }
  .feature-title {
    display: block;
    font-size: 40px;
    font-weight: 700;
    letter-spacing: 0.5px;
  }
  .feature-detail {
    display: block;
    margin-top: 10px;
    font-size: 32px;
    font-weight: 400;
    letter-spacing: 2px;
  }
</style>
</head>
<body>
  <section class="billboard">
    <div class="brand-panel">
      <p class="park-name">Cedar Bend RV park</p>
      <div class="phone-band">
        <p class="phone-number">(409) 555-0142</p>
      </div>
    </div>
    <div class="features-panel">
      <svg class="feature-icon feature-icon--fiber" viewBox="0 0 90 88" aria-hidden="true">
        <g fill="none" stroke="#ffffff" stroke-width="2.5" stroke-linecap="round">
          <path d="M45 47 L45 6"/>
          <path d="M43 47 C40 38 34 30 19 24"/>
          <path d="M47 47 C50 38 56 30 71 24"/>
          <path d="M44 47 C38 36 30 30 27 24"/>
          <path d="M46 47 C52 36 60 30 63 24"/>
        </g>
        <g fill="#ffffff">
          <circle cx="45" cy="5" r="4.5"/>
          <circle cx="17" cy="23" r="4.5"/>
          <circle cx="73" cy="23" r="4.5"/>
          <rect x="42" y="44" width="6" height="8"/>
          <rect x="33" y="52" width="24" height="36"/>
        </g>
      </svg>
      <div class="feature-text feature-text--fiber">
        <span class="feature-title">Free fiber optic</span>
        <span class="feature-detail">internet</span>
      </div>

      <svg class="feature-icon feature-icon--wifi" viewBox="0 0 90 70" aria-hidden="true">
        <g fill="none" stroke="#ffffff" stroke-width="9" stroke-linecap="round">
          <path d="M5 22 C28 -2 62 -2 85 22"/>
          <path d="M19 36 C34 20 56 20 71 36"/>
          <path d="M33 49 C40 42 50 42 57 49"/>
        </g>
        <circle cx="45" cy="63" r="6.5" fill="#ffffff"/>
      </svg>
      <div class="feature-text feature-text--wifi">
        <span class="feature-title">Personal hotspot</span>
        <span class="feature-detail">for each camper</span>
      </div>
    </div>
  </section>
</body>
</html>
```